Refresh our Logo and Letterhead!

We would like to see designs with blue, green, teal etc. Our current logo and contact details for the letterhead is attached.
We're a small boutique firm based in Sydney, Australia. We're near the coast and not opposed to coastal images. We practice in property law and have primarily female practitioners, although we don't necessarily need the logo and letterhead to be too feminine. We would like to see designs with blue, green, teal etc. Our current logo and contact details for the letterhead is attached.
We're a small boutique firm based in Sydney, Australia. We're near the coast and not opposed to coastal images. We practice in property law and have primarily female practitioners, although we don't necessarily need the logo and letterhead to be too feminine.

Target Market(s)

Young professionals

Industry/Entity Type

Law Firm

Logo Text

Halvering Legal

Font styles to use
Serif
Sans Serif

Colors
34a7d8
00a990
85acd3
886aae

Requirements
Must have
• The letterhead must have the text in the "contact info" jpg uploaded with the brief.
Nice to have
• We'd like to see some simple, innovating, fresh ideas. A watermark or something interesting in the background would be good.

```html
<!DOCTYPE html>
<html lang="en">
<head>
<meta charset="utf-8">
<title>Halvering Legal — Letterhead</title>
<link rel="stylesheet" href="https://fonts.googleapis.com/css2?family=Didact+Gothic&family=Open+Sans:wght@400;600&display=swap">
<style>
  :root {
    --backdrop: #9fd9f0;
    --paper: #ffffff;
    --ink: #2b2f36;
    --brand-blue: #1f63a8;
    --brand-sky: #34a7d8;
    --brand-deep: #1b4f9c;
    --watermark: rgba(52, 100, 160, 0.07);
  }
  * { box-sizing: border-box; margin: 0; padding: 0; }
  html, body { width: 1200px; height: 898px; overflow: hidden; }
  body {
    background: var(--backdrop);
    display: flex; align-items: center; justify-content: center;
    font-family: "Didact Gothic", sans-serif;
    color: var(--ink);
  }
  .letterhead {
    position: relative;
    width: 608px; height: 860px;
    background: var(--paper);
    box-shadow: 0 6px 24px rgba(20, 80, 120, 0.25);
    overflow: hidden;
  }
  .masthead { position: absolute; top: 70px; left: 0; right: 0; }
  .brand {
    text-align: center;
    font-family: "Didact Gothic", sans-serif;
    color: var(--brand-blue);
  }
  .brand-name { font-size: 46px; letter-spacing: 1px; line-height: 1; }
  .brand-sub { font-size: 9px; letter-spacing: 8px; margin-top: 6px; }
  .masthead-rule {
    margin: 14px auto 0; width: 380px; height: 1.5px; background: var(--brand-blue);
  }
  .address {
    text-align: center; margin-top: 8px;
    font-family: "Open Sans", sans-serif; font-weight: 600;
    font-size: 11px; letter-spacing: 2.4px; color: var(--brand-blue);
  }
  .watermark {
    position: absolute; left: 214px; top: 320px;
    width: 180px; height: 180px; border-radius: 50%;
    background: var(--watermark);
  }
  .body-copy {
    position: absolute; top: 232px; left: 70px; right: 70px;
    font-size: 12px; line-height: 1.55; text-align: center;
  }
  .body-copy p + p { margin-top: 20px; }
  .signature {
    position: absolute; top: 664px; right: 76px; text-align: left;
  }
  .signature-name { font-size: 16px; line-height: 1.2; }
  .signature-role { font-size: 10px; margin-top: 4px; }
  .footer-rule {
    position: absolute; top: 738px; left: 60px; right: 60px;
    height: 1.5px; background: var(--brand-blue);
  }
  .contacts {
    position: absolute; top: 752px; left: 0; right: 0;
    display: flex; justify-content: center; gap: 16px;
    font-family: "Open Sans", sans-serif; font-size: 9.5px; color: var(--ink);
  }
  .contact { display: flex; align-items: center; gap: 4px; }
  .contact svg { width: 11px; height: 11px; fill: var(--brand-blue); }
  .web {
    position: absolute; top: 776px; left: 0; right: 0; text-align: center;
    font-family: "Open Sans", sans-serif; font-size: 10px;
    letter-spacing: 5px; color: var(--brand-blue);
  }
  .footer-band {
    position: absolute; bottom: 0; left: 0; right: 0; height: 22px;
    background: linear-gradient(90deg, var(--brand-sky), var(--brand-deep));
  }
</style>
</head>
<body>
<main class="letterhead">
  <header class="masthead">
    <div class="brand">
      <div class="brand-name">Halvering</div>
      <div class="brand-sub">LEGAL PTY LTD</div>
    </div>
    <div class="masthead-rule"></div>
    <div class="address">14 Marlowe Bay Road Avoca NSW 2251</div>
  </header>

  <div class="watermark" aria-hidden="true"></div>

  <section class="body-copy">
    <p>Lorem ipsum dolor sit amet, consectetur adipiscing elit. Donec orci purus, luctus vitae dignissim eu, iaculis sed purus. Vivamus faucibus, ipsum nec aliquet viverra, leo mauris condimentum ligula, sit amet sagittis enim ligula quis arcu. Nam egestas tortor id nisi porttitor mattis. In tortor ante, ultricies in suscipit a, tempus non massa. Vivamus et auctor mi. Fusce vel massa nulla. Phasellus nec eros mauris, et scelerisque orci. Donec malesuada orci vitae nulla accumsan porta a id massa.</p>
    <p>Quisque accumsan iaculis magna sit amet fringilla. Maecenas consequat, magna eget tincidunt semper, odio nibh rutrum mi, id feugiat ante nisi eu risus. Vestibulum nunc orci, rhoncus a placerat in, ultricies in mi. Cras mattis varius eros, vel fringilla nisi suscipit eget. Quisque scelerisque sagittis nulla at porttitor. Mauris a justo et tellus interdum tristique. Sed id augue vitae urna euismod commodo aliquet a quam. Pellentesque arcu velit, cursus et malesuada ut, consequat et diam. Nullam erat sem, rhoncus id ullamcorper vitae, rhoncus et arcu. In ultricies ultricies nulla.</p>
    <p>Kut rutrum nisi iaculis at. Donec eu magna a metus ornare faucibus. Fusce aliquet faucibus ultricies. Morbi semper, est id tincidunt gravida, sem arcu adipiscing lacus, ac bibendum nulla leo eu purus. Quisque nec diam sed risus consectetur a accumsan quis quis nibh. Vestibulum id purus lorem. Donec eu magna a metus ornare faucibus. Fusce aliquet faucibus ultricies. Morbi semper, est id tincidunt gravida, sem arcu adipiscing lacus, ac bibendum nulla leo eu purus. Quisque nec diam sed risus consectetur a ccumsan quis quis nibh. Vestibulum id purus lorem.</p>
  </section>

  <div class="signature">
    <div class="signature-name">Owen Carrick</div>
    <div class="signature-role">Co-Founder &amp; CEO</div>
  </div>

  <div class="footer-rule"></div>
  <footer>
    <div class="contacts">
      <span class="contact"><svg viewBox="0 0 24 24" aria-hidden="true"><path d="M2 9c0-3 5-5 10-5s10 2 10 5v2h-5V9c-1-1-3-1.5-5-1.5S8 8 7 9v2H2zM6 12h12l3 8H3z"/></svg>02 4310 2867</span>
      <span class="contact"><svg viewBox="0 0 24 24" aria-hidden="true"><path d="M2 9c0-3 5-5 10-5s10 2 10 5v2h-5V9c-1-1-3-1.5-5-1.5S8 8 7 9v2H2zM6 12h12l3 8H3z"/></svg>0491 570 156</span>
      <span class="contact"><svg viewBox="0 0 24 24" aria-hidden="true"><path d="M2 9c0-3 5-5 10-5s10 2 10 5v2h-5V9c-1-1-3-1.5-5-1.5S8 8 7 9v2H2zM6 12h12l3 8H3z"/></svg>02 8011 4429</span>
      <span class="contact"><svg viewBox="0 0 24 24" aria-hidden="true"><path d="M2 5h20v14H2zM3 6l9 7 9-7" stroke="#fff" stroke-width="1.5"/></svg>mara@halveringlegal.com.au</span>
    </div>
    <div class="web">www.halvering.com</div>
    <div class="footer-band"></div>
  </footer>
</main>
</body>
</html>
```